依頼詳細
新設法人の名刺デザインを依頼致します。
記載項目
表面:企業ロゴ、社名、肩書、氏名、住所、電話番号、FAX番号、携帯番号、
メールアドレス、ホームページアドレス
裏面:企業ロゴ、(キャッチコピー)
希望イメージ
シンプル 複雑
単色 カラフル
暗い 明るい
日常 高級
遊び心 厳粛
未来的 伝統的
女性的 男性的
希望する色
納品ファイル
• イラストレーター形式 (.ai)
• PNG形式 (.png)
補足説明
イラストレーター形式とネット印刷会社への入稿用にPDF形式も頂きたいです。

此方の要望にも柔軟に応じていただき、非常に良いデザインに仕上がりました。
背面のデザインが特に気に入っています。

この度は弊社のコンペに応募いただき、ありがとうございました。
どのデザインも非常に精度の高いものであり、選定に非常に悩みました。
また機会がございましたら、何卒よろしくお願い致します。

```html
<!DOCTYPE html>
<html lang="ja">
<head>
<meta charset="utf-8">
<title>HARMORE Business Card</title>
<link rel="stylesheet" href="https://fonts.googleapis.com/css2?family=Noto+Sans+JP:wght@400;500;700&family=Roboto:wght@400;500;700&display=swap">
<style>
  :root {
    --board: #d6d6d6;
    --label: #4a4a4a;
    --brand: #1f4fa6;
    --ink: #222222;
    --muted: #555555;
    --rule: #9a9a9a;
    --paper: #ffffff;
  }
  * { margin: 0; padding: 0; box-sizing: border-box; }
  html, body { width: 805px; height: 1200px; overflow: hidden; }
  body {
    background: var(--board);
    font-family: "Noto Sans JP", "Roboto", sans-serif;
    color: var(--ink);
    position: relative;
  }
  .side-label {
    position: absolute;
    left: 54px;
    font-family: "Roboto", sans-serif;
    font-size: 19px;
    color: var(--label);
  }
  .side-label.front { top: 70px; }
  .side-label.back { top: 662px; }

  .card {
    position: absolute;
    left: 38px;
    width: 735px;
    box-shadow: 0 3px 10px rgba(0,0,0,0.25);
  }
  .card-front { top: 110px; height: 525px; background: var(--paper); }
  .card-back { top: 703px; height: 417px; background: var(--brand); }

  .edge-band {
    position: absolute; left: 0; top: 0;
    width: 22px; height: 440px;
    background: var(--brand);
  }

  .brand {
    position: absolute;
    display: flex; flex-direction: column; align-items: center;
  }
  .brand-mark {
    width: 74px; height: 74px; border-radius: 50%;
    background: var(--brand);
    margin-bottom: 14px;
  }
  .brand-name {
    font-family: "Roboto", sans-serif;
    font-weight: 500;
    font-size: 38px;
    letter-spacing: 1px;
    color: var(--brand);
    line-height: 1;
  }
  .brand-tagline {
    font-family: "Roboto", sans-serif;
    font-weight: 500;
    font-size: 13px;
    color: var(--brand);
    margin-top: 5px;
  }
  .card-front .brand { left: 50px; top: 145px; width: 230px; }

  .card-back .brand { left: 0; right: 0; top: 148px; flex-direction: row; justify-content: center; align-items: center; gap: 14px; }
  .card-back .brand-mark { background: var(--paper); width: 54px; height: 54px; margin: 0; }
  .card-back .brand-text { display: flex; flex-direction: column; }
  .card-back .brand-name { color: var(--paper); font-size: 44px; }
  .card-back .brand-tagline { color: var(--paper); font-size: 14px; }

  .details { position: absolute; left: 327px; right: 12px; top: 110px; }
  .title { font-size: 16px; color: var(--ink); }
  .person { display: flex; align-items: baseline; gap: 22px; margin-top: 6px; }
  .person-name { font-size: 36px; font-weight: 500; letter-spacing: 6px; }
  .person-roman { font-family: "Roboto", sans-serif; font-size: 15px; color: var(--muted); }
  .rule { height: 1px; background: var(--rule); margin: 6px 0 10px; }
  .line { display: flex; align-items: center; gap: 6px; font-size: 16px; color: var(--muted); line-height: 23px; }
  .icon { width: 16px; height: 16px; flex: none; }
  .company { font-size: 20px; color: var(--ink); margin-top: 22px; }
  .address-indent { padding-left: 22px; }
  .pair { display: flex; gap: 10px; }
  .url {
    font-family: "Roboto", sans-serif;
    font-size: 20px; font-weight: 500;
    color: var(--brand); margin-top: 12px;
  }
</style>
</head>
<body>
  <div class="side-label front">Front</div>
  <section class="card card-front">
    <div class="edge-band"></div>
    <div class="brand">
      <div class="brand-mark"></div>
      <div class="brand-name">HARMORE</div>
      <div class="brand-tagline">Quality For Every Day</div>
    </div>
    <div class="details">
      <div class="title">代表取締役</div>
      <div class="person">
        <span class="person-name">青木 一郎</span>
        <span class="person-roman">Ichiro Aoki</span>
      </div>
      <div class="rule"></div>
      <div class="line">
        <svg class="icon" viewBox="0 0 16 16"><rect width="16" height="16" rx="2" fill="#1f4fa6"/><rect x="5" y="3" width="6" height="10" rx="1" fill="#fff"/></svg>
        090-0000-0000
      </div>
      <div class="company">株式会社ハルモア</div>
      <div class="rule"></div>
      <div class="line">
        <svg class="icon" viewBox="0 0 16 16"><rect width="16" height="16" rx="2" fill="#1f4fa6"/><path d="M3 8 L8 3.5 L13 8 V13 H3 Z" fill="#fff"/></svg>
        〒123-0000
      </div>
      <div class="line address-indent">東京都○○○○○1-2-34○○○○○○</div>
      <div class="line pair">
        <span class="line">
          <svg class="icon" viewBox="0 0 16 16"><rect width="16" height="16" rx="2" fill="#1f4fa6"/><path d="M5 3 L7 5 L6 7 Q7 9 9 10 L11 9 L13 11 L11 13 Q5 12 3 5 Z" fill="#fff"/></svg>
          03-0000-0000
        </span>
        <span class="line">
          <svg class="icon" viewBox="0 0 16 16"><rect width="16" height="16" rx="2" fill="#1f4fa6"/><rect x="3" y="6" width="10" height="7" fill="#fff"/><rect x="5" y="3" width="6" height="3" fill="#fff"/></svg>
          03-0000-0000
        </span>
      </div>
      <div class="line">
        <svg class="icon" viewBox="0 0 16 16"><rect width="16" height="16" rx="2" fill="#1f4fa6"/><rect x="3" y="4.5" width="10" height="7" fill="#fff"/><path d="M3 4.5 L8 9 L13 4.5" stroke="#1f4fa6" fill="none"/></svg>
        info@example.com
      </div>
      <div class="url">http://www.example.com</div>
    </div>
  </section>

  <div class="side-label back">Back</div>
  <section class="card card-back">
    <div class="brand">
      <div class="brand-mark"></div>
      <div class="brand-text">
        <div class="brand-name">HARMORE</div>
        <div class="brand-tagline">Quality For Every Day</div>
      </div>
    </div>
  </section>
</body>
</html>
```